property investment and development company needs a website

we need a website that looks professional and portrays trust for people looking to us to buy their house or investors looking to invest or joint venture with us.
We are based in the west midlands in the UK.
we deal mainly with residential housing, house to flats conversions, HMO's (houses in multiple ocupancy).
we require the website as a first point of contact with potential sellers, renters and investors so links or contact details that are easy to access or see would be good.
I have had logos designed by a brisk easel member and these can be used as guidance for the colour and style of the site.
Target Market(s)
joint venture investment partners, people looking to sell their house, people looking to rent from us.
Coding
Coded - Design and coding required
Number of Pages Required
3 page
Requirements
Must have
- project a professional appearance
- visable contact details

```html
<!DOCTYPE html>
<html lang="en">
<head>
<meta charset="utf-8">
<title>Calder Homes</title>
<link rel="stylesheet" href="https://fonts.googleapis.com/css2?family=Cinzel:wght@700&family=Montserrat:wght@700&family=Nunito+Sans:wght@400;600&display=swap">
<style>
:root{
  --navy:#232a38;
  --navy-deep:#1b212c;
  --gold:#b8955a;
  --gold-light:#cfae72;
  --gold-dark:#a5824a;
  --text:#6b6b6b;
  --white:#ffffff;
  --field:rgba(255,255,255,0.55);
}
*{margin:0;padding:0;box-sizing:border-box}
html,body{width:1200px;height:3219px;overflow:hidden}
body{position:relative;background:var(--white);font-family:"Nunito Sans",Arial,sans-serif;color:var(--text)}
.abs{position:absolute}
.serif{font-family:"Cinzel",Georgia,serif;font-weight:700}
.center{left:0;width:1200px;text-align:center}

/* hero */
.hero-photo{left:0;top:0;width:1200px;height:615px;background:linear-gradient(180deg,#1e2838 0%,#3a3a42 35%,#6a4d38 60%,#8a7e72 85%,#5d5a55 100%)}
.hero-shade{left:0;top:0;width:1200px;height:615px;background:rgba(20,25,35,0.25)}
.brand-tab{left:485px;top:0;width:230px;height:172px}
.brand-name{left:485px;top:46px;width:230px;text-align:center;font-family:"Cinzel",Georgia,serif;font-weight:700;font-size:25px;line-height:29px;color:var(--gold-light);letter-spacing:1px}
.hero-title{top:283px;font-family:"Montserrat",Arial,sans-serif;font-weight:700;font-size:86px;line-height:96px;color:var(--white);letter-spacing:-1px}
.hero-sub{top:390px;font-size:18px;line-height:27px;color:var(--white)}

/* nav */
.main-nav{left:0;top:615px;width:1200px;height:62px;background:var(--navy)}
.nav-item{top:0;height:62px;line-height:62px;font-family:"Montserrat",Arial,sans-serif;font-weight:400;font-size:15px;color:var(--white);text-align:center;transform:translateX(-50%);white-space:nowrap}
.nav-item.active{left:297px;width:126px;transform:none;background:linear-gradient(180deg,var(--gold-light),var(--gold-dark))}
.nav-sep{top:16px;width:1px;height:32px;background:rgba(255,255,255,0.25)}

/* buttons */
.btn{height:57px;line-height:57px;border-radius:5px;text-align:center;font-family:"Cinzel",Georgia,serif;font-weight:700;font-size:21px;color:var(--white);background:linear-gradient(180deg,var(--gold-light),var(--gold-dark));box-shadow:0 2px 3px rgba(0,0,0,0.2);letter-spacing:1px}

/* welcome */
.welcome-kicker{top:736px;font-size:24px;color:var(--navy)}
.welcome-title{top:768px;font-size:48px;color:var(--navy)}
.welcome-copy{left:255px;width:690px;text-align:center;font-size:14px;line-height:27px;color:var(--text)}

/* services */
.band{left:0;width:1200px;background:var(--navy)}
.band-title{font-size:48px;color:var(--white)}
.services-photo{left:0;top:1260px;width:1200px;height:532px;background:linear-gradient(180deg,#2c2a2c 0%,#3e342f 45%,#231f1f 100%)}
.icon-circle{width:134px;height:134px;border-radius:50%;background:var(--white)}
.service-head{top:1450px;font-size:32px;color:var(--white)}
.service-copy{font-size:14px;line-height:27px;color:#e5e5e5}

/* testimonials */
.testi-title{top:1845px;font-size:48px;color:var(--navy)}
.testi-copy{left:305px;width:590px;text-align:center;font-size:14px;line-height:27px;color:var(--text)}
.client-name{top:2128px;font-size:19px;color:var(--gold)}
.dot{top:2171px;width:10px;height:10px;border-radius:50%;background:#cfcfcf}
.dot.on{background:var(--white);border:1.5px solid var(--gold)}

/* contact */
.contact-photo{left:0;top:2359px;width:1200px;height:465px;background:linear-gradient(90deg,#3a302c 0%,#4b3e38 40%,#5a5350 70%,#3f3d3f 100%)}
.contact-shade{left:0;top:2359px;width:1200px;height:465px;background:rgba(20,24,32,0.35)}
.contact-lead{top:2391px;font-size:16px;font-weight:600;color:var(--white)}
.field{background:var(--field);border-radius:3px;font-size:13px;color:var(--white);padding:14px 23px;border:1px solid transparent}
.field.focus{border-color:var(--gold);background:rgba(255,255,255,0.12);color:var(--gold-light)}
.check-label{top:2657px;font-size:13px;color:var(--white)}
.check-box{top:2659px;width:15px;height:15px;background:var(--white)}

/* footer */
.social{top:2974px;width:41px;height:41px;border-radius:2px;background:#cfcfcf}
.social.on{background:var(--gold)}
.footer-line{font-size:14px;line-height:22px;color:#5b5b5b}
.footer-line a{color:var(--gold);text-decoration:none}
.to-top{left:575px;top:3121px;width:50px;height:37px;background:var(--navy);border-radius:4px 4px 0 0}
.legal{left:0;top:3158px;width:1200px;height:61px;background:var(--navy);text-align:center;line-height:61px;font-size:13px;color:#d8d8d8}
</style>
</head>
<body>

<header>
  <div class="abs hero-photo" role="img" aria-label="Photograph of a modern timber-clad family house lit up at dusk"></div>
  <div class="abs hero-shade"></div>
  <svg class="abs brand-tab" viewBox="0 0 230 172" aria-hidden="true"><polygon points="0,0 230,0 230,132 115,172 0,132" fill="#2a3140" opacity="0.92"/></svg>
  <div class="abs brand-name">CALDER<br>HOMES</div>
  <h1 class="abs center hero-title">CALDER HOMES</h1>
  <p class="abs center hero-sub">We ensure that whatever your property needs are we deliver<br>bespoke services for our clients</p>

  <nav class="abs main-nav">
    <span class="abs nav-item active">HOME</span>
    <span class="abs nav-item" style="left:495px">INVEST</span>
    <span class="abs nav-sep" style="left:560px"></span>
    <span class="abs nav-item" style="left:618px">SELL</span>
    <span class="abs nav-sep" style="left:674px"></span>
    <span class="abs nav-item" style="left:744px">ABOUT US</span>
    <span class="abs nav-sep" style="left:810px"></span>
    <span class="abs nav-item" style="left:893px">CONTACT US</span>
  </nav>
</header>

<section class="welcome">
  <h3 class="abs center serif welcome-kicker">WELCOME TO</h3>
  <h2 class="abs center serif welcome-title">CALDER HOMES</h2>
  <p class="abs welcome-copy" style="top:844px">We are a property development and investment company that have our own portfolio and we are active investors who pride ourselves in expanding our business organically.</p>
  <p class="abs welcome-copy" style="top:916px">We ensure that whatever your property needs are we deliver bespoke services for our clients. For investors, sellers, landlords and tenants we bring knowledge to your next property decision, allowing you to make an informed decision.</p>
  <div class="abs btn" style="left:509px;top:1022px;width:182px">LEARN MORE</div>
</section>

<section class="services">
  <div class="abs band" style="top:1146px;height:114px"></div>
  <h2 class="abs center serif band-title" style="top:1172px">CALDER HOMES</h2>
  <div class="abs services-photo" role="img" aria-label="Photograph of a brick family home at dusk with warm lit windows"></div>

  <div class="abs icon-circle" style="left:464px;top:1298px"></div>
  <svg class="abs" style="left:497px;top:1325px" width="70" height="80" viewBox="0 0 70 80" fill="none" stroke="#b8955a" stroke-width="2.5" aria-hidden="true">
    <rect x="6" y="10" width="38" height="56" rx="2"/>
    <rect x="14" y="18" width="38" height="56" rx="2"/>
    <circle cx="30" cy="44" r="9"/>
    <path d="M48 46 a10 10 0 1 1 -6 16 M42 62 l0 -6 M42 62 l6 0"/>
    <path d="M52 14 l12 6 l-10 26"/>
  </svg>

  <div class="abs icon-circle" style="left:633px;top:1298px"></div>
  <svg class="abs" style="left:665px;top:1325px" width="70" height="80" viewBox="0 0 70 80" fill="none" stroke="#b8955a" stroke-width="2.5" aria-hidden="true">
    <path d="M6 36 L35 8 L64 36"/>
    <path d="M14 30 V72 H56 V30"/>
    <circle cx="35" cy="50" r="14"/>
    <path d="M40 43 c-2 -3 -10 -3 -10 1 c0 5 11 3 11 9 c0 4 -9 4 -11 1 M35 38 V62"/>
  </svg>

  <h3 class="abs serif service-head" style="left:400px;width:196px;text-align:right">INVEST</h3>
  <h3 class="abs serif service-head" style="left:636px">SELL</h3>

  <p class="abs service-copy" style="left:205px;top:1499px;width:389px;text-align:right">We have our own portfolio and we are active investors, so our finger is on the pulse and we are currently looking for residential development investments &amp; commercial to residential conversions in cities or regional centres showing strong growth.</p>
  <p class="abs service-copy" style="left:634px;top:1499px;width:425px">We undertake the necessary market research to evaluate an option that works for all parties involved. We will help guide you to make an informed decision on how to gain the maximum realistic value. For those looking to achieve a fast and professional sale to experienced investors</p>

  <div class="abs btn" style="left:409px;top:1659px;width:182px">LEARN MORE</div>
  <div class="abs btn" style="left:636px;top:1659px;width:183px">LEARN MORE</div>
</section>

<section class="testimonials">
  <h2 class="abs center serif testi-title">WHAT OUR CLIENT SAY</h2>
  <svg class="abs" style="left:563px;top:1925px" width="74" height="74" viewBox="0 0 74 74" aria-hidden="true">
    <circle cx="37" cy="37" r="35" fill="none" stroke="#b8955a" stroke-width="2.5"/>
    <text x="37" y="58" text-anchor="middle" font-family="Georgia,serif" font-size="50" font-weight="700" fill="#b8955a">&#8220;</text>
  </svg>
  <p class="abs testi-copy" style="top:2023px">&#8220; Lorem Ipsum is simply dummy text of the printing and typesetting industry. Lorem Ipsum has been the industry's standard dummy text ever since the 1500s, when an unknown printer took a galley of type. &#8221;</p>
  <p class="abs center serif client-name">&#8211; CLIENT NAME</p>
  <span class="abs dot" style="left:564px"></span>
  <span class="abs dot" style="left:580px"></span>
  <span class="abs dot on" style="left:595px"></span>
  <span class="abs dot" style="left:611px"></span>
  <span class="abs dot" style="left:626px"></span>
</section>

<section class="contact">
  <div class="abs band" style="top:2244px;height:115px"></div>
  <h2 class="abs center serif band-title" style="top:2270px">CONTACT US</h2>
  <div class="abs contact-photo" role="img" aria-label="Photograph of a couple meeting a property adviser at a desk with a laptop"></div>
  <div class="abs contact-shade"></div>
  <p class="abs center contact-lead">Get in touch, let's work together</p>

  <div class="abs field focus" style="left:96px;top:2451px;width:500px;height:51px">Name</div>
  <div class="abs field" style="left:96px;top:2514px;width:500px;height:51px">E-Mail</div>
  <div class="abs field" style="left:96px;top:2576px;width:500px;height:51px">Phone</div>
  <div class="abs field" style="left:607px;top:2451px;width:500px;height:176px">Message</div>

  <span class="abs check-label" style="left:396px">SELLERS</span>
  <span class="abs check-box" style="left:478px"></span>
  <span class="abs check-label" style="left:539px">RENTERS</span>
  <span class="abs check-box" style="left:625px"></span>
  <span class="abs check-label" style="left:692px">INVESTORS</span>
  <span class="abs check-box" style="left:788px"></span>

  <div class="abs btn" style="left:509px;top:2704px;width:181px">SUBMIT</div>
</section>

<footer>
  <div class="abs band" style="top:2824px;height:94px"></div>
  <h2 class="abs center serif" style="top:2848px;font-size:35px;color:#fff">KEEP IN TOUCH</h2>

  <span class="abs social on" style="left:530px" aria-label="Social profile one"></span>
  <span class="abs social" style="left:579px" aria-label="Social profile two"></span>
  <span class="abs social" style="left:629px" aria-label="Social profile three"></span>

  <p class="abs center footer-line" style="top:3033px">01632 960418 | <a href="#">hello@calderhomes.example</a></p>
  <p class="abs center footer-line" style="top:3055px">12 Harrow Lane, Fenwick, Westshire, FX1 4QP</p>

  <div class="abs to-top"></div>
  <svg class="abs" style="left:590px;top:3131px" width="20" height="18" viewBox="0 0 20 18" fill="none" stroke="#b8955a" stroke-width="2" aria-hidden="true">
    <path d="M4 9 L10 3 L16 9 M4 15 L10 9 L16 15"/>
  </svg>

  <div class="abs legal">©CALDER HOMES - 2019 All Rights Reserved.</div>
</footer>

</body>
</html>
```